Ridgeway Brew Label design/Graphic design

The Company
Ridgeway brew is an exciting new brand of ‘fit beer’ targeted at fitness enthusiasts as well as beer lovers. Ridgeway brew is a craft beer with added protein which can be used as a post work out recovery/leisure beverage. The target audience is generally male, 18-30 years old.
We need label/graphic design of the product to appear on our website www.ridgewaybrew.co.uk

The Project
The project is to submit four designs, one for each flavour:
• Larger
• Honey Ale
• Banana Ale
• Zero Alcohol

The design of each flavour must be differentiated, yet have a consistent theme throughout all flavours. At this point Ridgeway brew has no official logo so feel free to incorporate this into the design, although this is not absolutely necessary.

The label/design should include the following basic information:
Brand name: Ridgeway Brew
Type: Larger/Honey Ale/Banana Ale/Zero
Tag: 7g High Quality Protein
Alcohol percentage: 4%/Vol (0%/Vol for the Zero alcohol version)
Volume: 300ml

Brand Guidelines (designs not necessarily limited to these)
Font: Aldrich
Main Colours: Blue # 005fbf Orange # ed7000
Basic beer bottle image attached.

The final design will be displayed on (but not limited to) the website www.ridgewaybrew.co.uk

The winning designer may be contacted for future projects and opportunities with Ridgeway Brew.

Project Deadline Extended
Reason: My apologies I have been sick the last few days and have been unable to provide feedback. Your work is much appreciated, I will extend the project to give us a little more time and provide feedback individually later today. Best Regards, Oliver

Target Market(s)

The target audience is generally male, 18-30 years old.

Industry/Entity Type

Fitness

Requirements
Must have
• The label/design should include the following basic information:
Brand name: Ridgeway Brew
Volume: 300ml

```html
<!DOCTYPE html>
<html lang="en">
<head>
<meta charset="utf-8">
<title>Ridgeway Brew – Flavour Labels</title>
<link rel="stylesheet" href="https://fonts.googleapis.com/css2?family=Cinzel:wght@400;600&family=Tinos&display=swap">
<style>
  :root {
    --page: #ffffff;
    --black: #0b0b0b;
    --panel-dark: #050505;
    --panel-mid: #3a3a3a;
    --gold-light: #fff3a8;
    --gold: #e2b93b;
    --gold-dark: #9a6f12;
    --text-gold: #e8cf7a;
    --figure-green: #1f6a5a;
    --figure-gold: #b98d2c;
    --larger: #8e1414;
    --honey: #f0a21d;
    --banana: #f3a414;
    --zero: #42d4e0;
  }
  * { box-sizing: border-box; margin: 0; padding: 0; }
  html, body { width: 929px; height: 1200px; overflow: hidden; background: var(--page); }
  .sheet { position: relative; width: 929px; height: 1200px; }

  .label {
    position: absolute;
    width: 372px;
    height: 510px;
    background: linear-gradient(135deg, var(--gold-light), var(--gold) 35%, var(--gold-dark) 65%, var(--gold) 100%);
    padding: 10px;
  }
  .label--larger { left: 71px;  top: 98px;  --flavour: var(--larger); }
  .label--honey  { left: 479px; top: 98px;  --flavour: var(--honey); }
  .label--banana { left: 71px;  top: 629px; --flavour: var(--banana); }
  .label--zero   { left: 479px; top: 629px; --flavour: var(--zero); }

  .label__panel {
    position: relative;
    width: 100%;
    height: 100%;
    background: radial-gradient(ellipse at 50% 35%, var(--panel-mid) 0%, #1a1a1a 40%, var(--panel-dark) 80%);
    border: 1px solid var(--gold-dark);
  }
  .label__dots {
    position: absolute;
    inset: 10px;
    border: 3px dotted var(--gold);
    border-radius: 10px;
  }

  .label__figure {
    position: absolute;
    left: 66px;
    top: 22px;
    width: 220px;
    height: 200px;
    border-radius: 40% 40% 20% 20%;
    background: radial-gradient(ellipse at 50% 45%, var(--figure-green) 0%, #174a40 45%, var(--figure-gold) 75%, rgba(185,141,44,0) 100%);
    opacity: .9;
  }

  .label__ribbon {
    position: absolute;
    left: 70px;
    top: 214px;
    width: 212px;
    height: 46px;
  }
  .label__ribbon svg { position: absolute; inset: 0; }
  .label__flavour {
    position: relative;
    display: block;
    line-height: 46px;
    text-align: center;
    font-family: "Cinzel", serif;
    font-size: 21px;
    font-weight: 600;
    color: var(--gold-light);
    text-shadow: 0 1px 1px rgba(0,0,0,.6);
  }
  .label--zero .label__flavour { font-size: 18px; }

  .label__brandband {
    position: absolute;
    left: -22px;
    right: -22px;
    top: 300px;
    height: 82px;
    background: linear-gradient(180deg, #2a2a2a, var(--black) 50%, #1f1f1f);
    border-top: 3px solid var(--gold);
    border-bottom: 3px solid var(--gold);
    box-shadow: 0 0 0 1px var(--gold-dark);
    display: flex;
    align-items: center;
    justify-content: center;
  }
  .label__brand {
    font-family: "Cinzel", serif;
    font-size: 40px;
    font-weight: 400;
    letter-spacing: .5px;
    color: var(--text-gold);
    white-space: nowrap;
  }

  .label__tag {
    position: absolute;
    left: 70px;
    right: 70px;
    top: 392px;
    height: 30px;
    border: 2px solid var(--gold);
    display: flex;
    align-items: center;
    justify-content: center;
    font-family: "Tinos", serif;
    font-size: 15px;
    color: var(--text-gold);
  }

  .label__meta {
    position: absolute;
    left: 30px;
    right: 30px;
    top: 448px;
    display: flex;
    justify-content: space-between;
    font-family: "Tinos", serif;
    font-size: 15px;
    color: var(--text-gold);
  }
</style>
</head>
<body>
<main class="sheet">

  <article class="label label--larger">
    <div class="label__panel">
      <div class="label__dots"></div>
      <div class="label__figure" role="img" aria-label="Illustration of a flexing muscular figure with gold flourishes"></div>
      <div class="label__ribbon">
        <svg viewBox="0 0 212 46" preserveAspectRatio="none"><path d="M0 4 L212 4 L200 23 L212 42 L0 42 L12 23 Z" fill="var(--flavour)" stroke="#e2b93b" stroke-width="2"/></svg>
        <span class="label__flavour">LARGER</span>
      </div>
      <div class="label__brandband"><span class="label__brand">RIDGEWAY BREW</span></div>
      <div class="label__tag">7g. High Quality Protein</div>
      <div class="label__meta"><span>300 ml</span><span>Alc.4%Vol</span></div>
    </div>
  </article>

  <article class="label label--honey">
    <div class="label__panel">
      <div class="label__dots"></div>
      <div class="label__figure" role="img" aria-label="Illustration of a flexing muscular figure with gold flourishes"></div>
      <div class="label__ribbon">
        <svg viewBox="0 0 212 46" preserveAspectRatio="none"><path d="M0 4 L212 4 L200 23 L212 42 L0 42 L12 23 Z" fill="var(--flavour)" stroke="#e2b93b" stroke-width="2"/></svg>
        <span class="label__flavour">HONEY ALE</span>
      </div>
      <div class="label__brandband"><span class="label__brand">RIDGEWAY BREW</span></div>
      <div class="label__tag">7g. High Quality Protein</div>
      <div class="label__meta"><span>300 ml</span><span>Alc.4%Vol</span></div>
    </div>
  </article>

  <article class="label label--banana">
    <div class="label__panel">
      <div class="label__dots"></div>
      <div class="label__figure" role="img" aria-label="Illustration of a flexing muscular figure with gold flourishes"></div>
      <div class="label__ribbon">
        <svg viewBox="0 0 212 46" preserveAspectRatio="none"><path d="M0 4 L212 4 L200 23 L212 42 L0 42 L12 23 Z" fill="var(--flavour)" stroke="#e2b93b" stroke-width="2"/></svg>
        <span class="label__flavour">BANANA ALE</span>
      </div>
      <div class="label__brandband"><span class="label__brand">RIDGEWAY BREW</span></div>
      <div class="label__tag">7g. High Quality Protein</div>
      <div class="label__meta"><span>300 ml</span><span>Alc.4%Vol</span></div>
    </div>
  </article>

  <article class="label label--zero">
    <div class="label__panel">
      <div class="label__dots"></div>
      <div class="label__figure" role="img" aria-label="Illustration of a flexing muscular figure with gold flourishes"></div>
      <div class="label__ribbon">
        <svg viewBox="0 0 212 46" preserveAspectRatio="none"><path d="M0 4 L212 4 L200 23 L212 42 L0 42 L12 23 Z" fill="var(--flavour)" stroke="#e2b93b" stroke-width="2"/></svg>
        <span class="label__flavour">ZERO ALCOHOL</span>
      </div>
      <div class="label__brandband"><span class="label__brand">RIDGEWAY BREW</span></div>
      <div class="label__tag">7g. High Quality Protein</div>
      <div class="label__meta"><span>300 ml</span><span>Alc.0%Vol</span></div>
    </div>
  </article>

</main>
</body>
</html>
```